web site update

I want to get a better website for a small high end remodeling and construction company
I currently have a web site but you will find that it is not good.
www.pelbrookhaven.com
We are a high end construction / remodeling company that has been in business since 2003. We primarily work in the mid peninsula of the bay area. Most of our clientele are very educated captains of industry. This group is still the target client.
I had my logo designed by Vellum Forge a few years ago and I do like it, I like the orange and black or orange a blue. I don’t have a lot of content on hand as far as professional photographs.
Number of pages not sure and are open to: design pages vs full function website
I think what I am after is a web presence that will seal the deal as we are getting high referrals from past clients.
Construction
1 page

```html
<!DOCTYPE html>
<html lang="en">
<head>
<meta charset="utf-8">
<title>Pelbrook Haven Remodeling</title>
<link rel="stylesheet" href="https://fonts.googleapis.com/css2?family=Open+Sans:ital,wght@0,300;0,400;0,600;0,700;1,300&display=swap">
<style>
:root{
  --orange:#ef5b12;
  --ink:#1a1a1a;
  --text:#555;
  --light:#ececec;
  --topbar:#e6e6e6;
  --black:#000;
  --footer-text:#9a9a9a;
}
*{margin:0;padding:0;box-sizing:border-box}
html,body{width:766px;height:1200px;overflow:hidden;background:#fff}
body{font-family:"Open Sans",Arial,sans-serif;color:var(--text);position:relative}
.abs{position:absolute}
.topbar{left:0;top:0;width:766px;height:30px;background:var(--topbar)}
.topbar .info{top:8px;font-size:6px;line-height:8px;color:#333;white-space:nowrap}
.topbar .sep{top:8px;width:1px;height:16px;background:#333}
.navbar{left:0;top:30px;width:766px;height:32px;background:#fff;box-shadow:0 1px 3px rgba(0,0,0,.15)}
.nav{top:44px;font-size:7px;font-weight:600;color:#222;letter-spacing:.2px}
.nav.active{color:var(--orange)}
.brand{left:46px;top:0;width:152px;height:62px;background:#fff;display:flex;align-items:center;gap:8px;padding-left:14px;z-index:2}
.brand .mark{width:26px;height:26px;background:var(--ink)}
.brand .name{font-size:12px;font-weight:700;color:var(--orange);line-height:13px}
.hero{left:0;top:62px;width:766px;height:384px;
  background:
    radial-gradient(ellipse 110px 80px at 610px 250px,rgba(240,190,40,.9),rgba(240,190,40,0) 100%),
    radial-gradient(ellipse 260px 60px at 380px 300px,rgba(250,248,244,.95),rgba(250,248,244,0) 100%),
    linear-gradient(180deg,#cdbba2 0%,#b79c78 30%,#9c8266 48%,#c8bdb0 62%,#ece7df 74%,#b07a48 86%,#6e3f1c 100%)}
.arrow{top:238px}
.dots{top:412px;left:340px;display:flex;gap:7px}
.dots span{width:11px;height:11px;border-radius:50%;background:rgba(255,255,255,.75);border:1px solid #ccc}
.dots span.on{background:var(--orange);border:2px solid #fff}
h2{position:absolute;font-size:18px;font-weight:400;color:var(--ink);letter-spacing:.3px}
p.body{position:absolute;font-size:8.9px;font-weight:300;line-height:16px;color:#444}
.thumbs{left:392px;top:555px;display:grid;grid-template-columns:repeat(5,56px);gap:6px 12px}
.thumbs div{height:53px}
.btn{background:var(--orange);color:#fff;font-size:7px;font-weight:600;display:flex;align-items:center;justify-content:center}
.services{left:0;top:718px;width:766px;height:274px;background:var(--light)}
.more{font-size:7px;color:var(--orange);font-weight:600}
h3{position:absolute;font-size:15px;font-weight:400;color:var(--ink)}
.card{left:506px;top:819px;width:212px;height:137px;background:#fff}
.avatar{left:583px;top:785px;width:58px;height:58px;border-radius:50%;background:#b8bcc2;border:4px solid #fff;box-shadow:0 0 3px rgba(0,0,0,.2)}
.quote{left:524px;top:860px;width:176px;text-align:center;font-size:8.5px;font-style:italic;font-weight:300;line-height:15.5px;color:#555}
.author{left:520px;top:920px;width:184px;text-align:right;padding-right:8px;font-size:9.5px;font-weight:600;color:var(--orange)}
.footer{left:0;top:992px;width:766px;height:182px;background:var(--black)}
.fhead{top:1018px;font-size:9.5px;font-weight:700;color:var(--orange)}
.flist{top:1043px;list-style:none;font-size:7.5px;color:var(--footer-text);line-height:17.6px}
.fcontact{left:277px;top:1046px;font-size:7.5px;color:var(--footer-text);line-height:12px}
.fcontact b{color:#ddd;font-weight:600}
.map{left:392px;top:1048px;width:154px;height:98px;background:linear-gradient(135deg,#ebe7dc 0%,#e2e6d8 55%,#d7e3cc 100%);border:1px solid #ccc}
.input{left:564px;top:1077px;width:154px;height:20px;background:#333;border:1px solid #444;font-size:7px;font-style:italic;color:#888;padding:5px 8px}
.bottom{left:0;top:1174px;width:766px;height:26px;background:#0a0a0a;border-top:1px solid var(--orange);font-size:6px;color:#666}
</style>
</head>
<body>
<div class="abs topbar">
  <svg class="abs" style="left:487px;top:9px" width="12" height="12" viewBox="0 0 24 24"><path fill="#222" d="M6.6 10.8a15 15 0 0 0 6.6 6.6l2.2-2.2c.3-.3.7-.4 1-.2 1.1.4 2.3.6 3.6.6.6 0 1 .4 1 1V20c0 .6-.4 1-1 1A17 17 0 0 1 3 4c0-.6.4-1 1-1h3.5c.6 0 1 .4 1 1 0 1.2.2 2.4.6 3.6.1.3 0 .7-.2 1z"/></svg>
  <div class="abs info" style="left:505px"><b style="font-weight:600">415.555.0142</b><br>office@pelbrook.com</div>
  <div class="abs sep" style="left:575px"></div>
  <svg class="abs" style="left:584px;top:7px" width="16" height="15" viewBox="0 0 24 22"><path fill="#222" d="M12 1 1 11h3v10h6v-6h4v6h6V11h3z"/></svg>
  <div class="abs info" style="left:612px">88 Alder Lane,<br>Mid Peninsula</div>
  <div class="abs sep" style="left:677px"></div>
  <div class="abs" style="left:689px;top:12px;width:7px;height:7px;border-radius:50%;background:#222"></div>
  <div class="abs" style="left:709px;top:12px;width:7px;height:7px;border-radius:50%;background:#222"></div>
</div>
<div class="abs navbar"></div>
<div class="abs brand"><div class="mark"></div><div class="name">PELBROOK<br>HAVEN</div></div>
<div class="abs nav active" style="left:443px">HOME</div>
<div class="abs nav" style="left:492px">ABOUT US</div>
<div class="abs nav" style="left:556px">SERVICES</div>
<div class="abs nav" style="left:615px">GALLERY</div>
<div class="abs nav" style="left:673px">CONTACT US</div>

<div class="abs hero" role="img" aria-label="Rolled blueprints and a yellow hard hat on a wooden desk in front of a city skyline with cranes"></div>
<svg class="abs arrow" style="left:16px" width="16" height="28" viewBox="0 0 16 28"><path d="M14 2 3 14l11 12" fill="none" stroke="#fff" stroke-width="2.5"/></svg>
<svg class="abs arrow" style="left:734px" width="16" height="28" viewBox="0 0 16 28"><path d="M2 2l11 12L2 26" fill="none" stroke="#fff" stroke-width="2.5"/></svg>
<div class="abs dots"><span class="on"></span><span></span><span></span><span></span><span></span></div>

<h2 style="left:46px;top:478px">WELCOME TO PELBROOK HAVEN</h2>
<p class="body" style="left:46px;top:512px;width:328px;text-align:justify">Contrary to popular belief, Lorem Ipsum is not simply random text. It has roots in a piece of classical Latin literature from 45 BC, making it over 2000 years old. Edwin Marsh, a Latin professor at Ashford College in Virginia, looked up one of the more obscure Latin words, consectetur, from a Lorem Ipsum passage, and going through</p>
<p class="body" style="left:46px;top:608px;width:328px;text-align:justify">the cites of the word in classical literature, discovered the undoubtable source. Lorem Ipsum comes from sections. classical literature, discovered the undoubtable source. Lorem Ipsum comes from sections. Latin professor at Ashford College in Virginia, looked up one of the more obscure Latin words Latin professor at Ashford College in Virginia, looked up one of the more obscure Latin words</p>

<h2 style="left:392px;top:478px">GALLERY</h2>
<p class="body" style="left:393px;top:512px;width:325px">Latin professor at Ashford College in Virginia, looked up one of the more obscure Latin words.</p>
<div class="abs thumbs">
  <div role="img" aria-label="Bedroom with wooden bed" style="background:linear-gradient(#5a3a26 0%,#e8d2b0 55%,#7a4a30 100%)"></div>
  <div role="img" aria-label="Living room interior" style="background:linear-gradient(90deg,#4e4e4a,#8e8c84 60%,#c9cbc6)"></div>
  <div role="img" aria-label="Kitchen with island" style="background:linear-gradient(#9aa2a6,#4a4640 55%,#6a6258)"></div>
  <div role="img" aria-label="Kitchen with tiled backsplash" style="background:linear-gradient(#6a3a26,#c89a6e 50%,#4a2e22)"></div>
  <div role="img" aria-label="House exterior among trees" style="background:linear-gradient(#8a8678,#3a3026 50%,#5a4a3a)"></div>
  <div role="img" aria-label="Modern kitchen with steel appliances" style="background:linear-gradient(90deg,#1e1e1e,#7a7a78 55%,#b8b8b4)"></div>
  <div role="img" aria-label="Exterior through trees" style="background:linear-gradient(#9a9484,#4a3c30 55%,#6a5a48)"></div>
  <div role="img" aria-label="Room with windows" style="background:linear-gradient(#2e2e2a,#a8b0a4 50%,#3a3a36)"></div>
  <div role="img" aria-label="Hallway interior" style="background:linear-gradient(#e6d6c8,#b88a78 55%,#8a5a4a)"></div>
  <div role="img" aria-label="Bedroom with wooden bed" style="background:linear-gradient(#7a5230 0%,#d8b888 55%,#3a3a5a 100%)"></div>
</div>
<div class="abs btn" style="left:630px;top:680px;width:88px;height:26px">FIND MORE</div>

<div class="abs services"></div>
<h2 style="left:46px;top:750px">OUR SERVICES</h2>
<div class="abs more" style="left:448px;top:758px">FIND MORE</div>
<h3 style="left:47px;top:788px">Construction</h3>
<h3 style="left:276px;top:788px">Remodelin</h3>
<div class="abs" role="img" aria-label="Building under construction with cranes" style="left:47px;top:819px;width:212px;height:80px;background:linear-gradient(100deg,#5a4a3a 0%,#8a7a68 45%,#6fa0d6 70%,#8ab6e2 100%)"></div>
<div class="abs" role="img" aria-label="Remodeled archway with recessed lights" style="left:277px;top:819px;width:212px;height:80px;background:radial-gradient(ellipse 90px 45px at 106px 60px,#f0dca8,rgba(240,220,168,0) 100%),linear-gradient(#5a4422,#a88a52)"></div>
<p class="body" style="left:46px;top:912px;width:213px;text-align:justify">There are many variations of passages of Lorem Ipsum available, but the majority have suffered alteration in some form, by injected humour</p>
<p class="body" style="left:277px;top:912px;width:212px;text-align:justify">There are many variations of passages of Lorem Ipsum available, but the majority have suffered alteration in some form, by injected humour</p>

<h2 style="left:507px;top:750px">TESTIMONIALS</h2>
<div class="abs more" style="left:678px;top:758px">FIND MORE</div>
<div class="abs card"></div>
<div class="abs avatar" role="img" aria-label="Client portrait"></div>
<div class="abs" style="left:522px;top:842px;font-size:18px;font-weight:700;color:#444;line-height:18px">&ldquo;</div>
<div class="abs quote">The standard chunk of Lorem Ipsum used since the 1500s is reproduced below for those interested.</div>
<div class="abs author">- Dale Hartwell -peninsula</div>

<div class="abs footer"></div>
<div class="abs fhead" style="left:47px">QUICK LINKS</div>
<div class="abs fhead" style="left:161px">SOCIAL MEDIA</div>
<div class="abs fhead" style="left:277px">CONTACT US</div>
<div class="abs fhead" style="left:564px">NEWSLETTER SUBSCRIBE</div>
<ul class="abs flist" style="left:47px"><li>Home</li><li>About us</li><li>Services</li><li>Gallery</li><li>Testimonials</li><li>Contact us</li></ul>
<ul class="abs flist" style="left:162px">
  <li><span style="display:inline-block;width:7px;height:7px;border-radius:50%;background:#777;margin-right:13px"></span>Chatterline</li>
  <li><span style="display:inline-block;width:7px;height:7px;border-radius:50%;background:#777;margin-right:13px"></span>Birdcall</li>
</ul>
<div class="abs fcontact"><b>Pelbrook Haven</b><br>88 Alder Lane,<br>Mid Peninsula<br><br>Phone: 415.555.0142<br>Email: office@pelbrook.com</div>
<div class="abs map" role="img" aria-label="Map of the mid peninsula area"></div>
<p class="abs" style="left:564px;top:1047px;width:154px;font-size:7px;color:var(--footer-text);line-height:12px">Regiter with your email address to get lates news about Pelbrook Haven</p>
<div class="abs input">Your Email Adress</div>
<div class="abs btn" style="left:565px;top:1101px;width:87px;height:26px;font-size:7.5px">Subscribe</div>

<div class="abs bottom">
  <span class="abs" style="left:47px;top:9px">Copyright © 2015 Pelbrook Haven</span>
  <span class="abs" style="right:48px;top:9px">Website Design: Tidewell Studio</span>
</div>
</body>
</html>
```